Business Card Design Project

Need a business card that stands my education platform as a whole but

Target Market(s)

Parents, families, expats in the middle east.

Industry/Entity Type

Education

Contact Information for Business Card

www.brightsprout.ae
www.thehomenest.ae
www.thecarecirclehub.ae

+971543192704
rebecca@brightsprout.ae

Font styles to use
Serif

Requirements
Must have
• Logo's and contact details

```html
<!DOCTYPE html>
<html lang="en">
<head>
<meta charset="utf-8">
<title>Bright Sprout – Business Card</title>
<link href="https://fonts.googleapis.com/css2?family=Source+Sans+3:wght@400;600;700&display=swap" rel="stylesheet">
<style>
  :root {
    --backdrop: #a9a9a9;
    --orange: #f4914a;
    --teal: #2f7f9c;
    --teal-deep: #3d8aa6;
    --paper: #ffffff;
  }
  * { margin: 0; padding: 0; box-sizing: border-box; }
  html, body { width: 1200px; height: 1048px; overflow: hidden; }
  body {
    background: var(--backdrop);
    font-family: "Source Sans 3", Arial, sans-serif;
    position: relative;
  }
  .card {
    position: absolute;
    left: 220px;
    width: 760px;
    height: 434px;
    overflow: hidden;
    box-shadow: 0 4px 14px rgba(0,0,0,0.18);
  }
  .card-front { top: 60px; background: var(--orange); }
  .card-back { top: 554px; background: var(--paper); }

  .front-emblem {
    position: absolute;
    left: 50%; top: 50%;
    width: 260px; height: 260px;
    transform: translate(-50%, -50%);
    border-radius: 50%;
    background: var(--paper);
    border: 2px solid var(--teal);
    display: flex; align-items: center; justify-content: center;
  }
  .brand-name {
    color: var(--teal);
    font-weight: 600;
    font-size: 32px;
    letter-spacing: 1px;
  }

  .back-band {
    position: absolute;
    left: 0; right: 0; bottom: 0;
    height: 150px;
    background: var(--orange);
  }
  .contact-list {
    position: absolute;
    left: 40px; top: 62px;
    display: grid;
    grid-template-columns: 88px auto;
    row-gap: 2px;
    font-size: 23px;
    line-height: 30px;
  }
  .contact-label { color: var(--orange); font-weight: 700; }
  .contact-value { color: var(--teal); font-weight: 400; letter-spacing: 0.5px; }

  .back-brand {
    position: absolute;
    right: 50px; top: 90px;
    width: 200px; height: 120px;
    display: flex; align-items: center; justify-content: center;
    gap: 12px;
  }
  .brand-dot {
    width: 18px; height: 18px;
    border-radius: 50%;
    background: var(--teal-deep);
  }
</style>
</head>
<body>
  <section class="card card-front" aria-label="Card front">
    <div class="front-emblem">
      <span class="brand-name">Bright Sprout</span>
    </div>
  </section>

  <section class="card card-back" aria-label="Card back">
    <div class="contact-list">
      <span class="contact-label">Web:</span><span class="contact-value">www.brightsprout.ae</span>
      <span></span><span class="contact-value">www.thehomenest.ae</span>
      <span></span><span class="contact-value">www.thecarecirclehub.ae</span>
      <span class="contact-label">Tell:</span><span class="contact-value">+971543192704</span>
      <span class="contact-label">Email:</span><span class="contact-value">rebecca@brightsprout.ae</span>
    </div>
    <div class="back-brand">
      <span class="brand-dot"></span>
      <span class="brand-name">Bright Sprout</span>
    </div>
    <div class="back-band"></div>
  </section>
</body>
</html>
```